Design a Shirt Hang Tag for a brand new streetwear company

We need a hang tag for our apparel. This will be attached and shipper with every shirt, hat, and hoodie. We make streetwear/urban apparel. For a feel of our products see http://loomferal.co

We'd like to see something die cut with a shape that isn't a rectangle.
Looking for a design that embodies "Savage". We are looking for something bold and fun. Our colors usually consist of black. white, and red, but if you feel like doing something else that you feel could fit our brand,go for it. Were savage, we don't want normal.

Target Market(s)

inner city, age 13-29, multi-cultural

Industry/Entity Type

Clothing

Font styles to use
Sans Serif
Other font styles liked:
• artist's choice

Colors
ec1f27
ffffff
000000

Requirements
Must have
• site url: www.loomferal.co
• Band Name: Loom Feral
• Double sided tag
• Die cut design

```html
<!DOCTYPE html>
<html lang="en">
<head>
<meta charset="utf-8">
<title>Loom Feral – Hang Tag</title>
<link rel="stylesheet" href="https://fonts.googleapis.com/css2?family=Oswald:wght@500;700&family=Montserrat:wght@700&display=swap">
<style>
  :root {
    --brand-red: #ec2227;
    --ink: #111212;
    --paper: #ffffff;
    --art-dark: #2a2a2a;
    --art-light: #d9d9d9;
    --deep-red: #a3141a;
    --sub-color: var(--deep-red);
  }
  html, body {
    margin: 0;
    padding: 0;
    width: 1053px;
    height: 1200px;
    overflow: hidden;
    background: var(--ink);
  }
  .presentation { display: block; width: 1053px; height: 1200px; }
  .panel-red { fill: var(--brand-red); }
  .panel-black { fill: var(--ink); }
  .tag-body { fill: var(--paper); }
  .title-band { fill: var(--ink); }
  .tag-title {
    font-family: "Oswald", sans-serif;
    font-weight: 700;
    fill: var(--paper);
  }
  .tag-subtitle {
    font-family: "Oswald", sans-serif;
    font-weight: 700;
    fill: var(--sub-color);
  }
  .size-label {
    font-family: "Oswald", sans-serif;
    font-weight: 500;
    fill: var(--ink);
  }
  .size-box { fill: none; stroke: var(--ink); stroke-width: 2; }
  .hang-hole { fill: var(--deep-red); }
  .side-label {
    font-family: "Montserrat", sans-serif;
    font-weight: 700;
    fill: var(--paper);
    letter-spacing: 3px;
  }
  .tag-set--on-black { --sub-color: var(--ink); }
</style>
</head>
<body>
<svg class="presentation" viewBox="0 0 1200 1367" preserveAspectRatio="none" xmlns="http://www.w3.org/2000/svg">
  <defs>
    <linearGradient id="artTone" x1="0" y1="0" x2="1" y2="1">
      <stop offset="0" stop-color="#d9d9d9"/>
      <stop offset="1" stop-color="#2a2a2a"/>
    </linearGradient>
    <filter id="tagShadow" x="-10%" y="-10%" width="130%" height="130%">
      <feDropShadow dx="6" dy="8" stdDeviation="4" flood-color="#5a0a0d" flood-opacity="0.6"/>
    </filter>

    <g id="tagFront">
      <path class="tag-body" d="M220 660 L220 380 L245 355 L300 305 L300 183 L490 183 L487 150 L500 138 L550 195 L555 210 L555 390 L562 395 L562 660 Z"/>
      <g role="img" aria-label="Illustration of a playing-card king holding a sword">
        <path fill="url(#artTone)" d="M232 495 L232 385 L255 362 L312 312 L318 195 L500 195 L500 160 L545 205 L545 395 L552 400 L552 495 Z"/>
      </g>
      <rect class="title-band" x="232" y="506" width="319" height="97"/>
      <text class="tag-title" x="391" y="589" text-anchor="middle" font-size="80" textLength="295" lengthAdjust="spacingAndGlyphs">LOOM FERAL</text>
      <text class="tag-subtitle" x="392" y="649" text-anchor="middle" font-size="40" letter-spacing="3" textLength="270" lengthAdjust="spacingAndGlyphs">WWW.LOOMFERAL.CO</text>
    </g>

    <g id="tagBack">
      <path class="tag-body" d="M843 548 L843 430 L860 412 L878 400 L878 350 L955 350 L958 333 L985 360 L985 548 Z"/>
      <circle class="hang-hole" cx="922" cy="368" r="3.5"/>
      <rect class="size-box" x="860" y="453" width="110" height="63"/>
      <line class="size-box" x1="893" y1="453" x2="893" y2="516"/>
      <line class="size-box" x1="860" y1="486" x2="893" y2="486"/>
      <text class="size-label" x="931" y="491" text-anchor="middle" font-size="15">SIZE</text>
      <text class="tag-subtitle" x="915" y="544" text-anchor="middle" font-size="18" textLength="112" lengthAdjust="spacingAndGlyphs">LOOM FERAL</text>
    </g>
  </defs>

  <rect class="panel-red" x="0" y="0" width="1200" height="804"/>
  <rect class="panel-black" x="0" y="804" width="1200" height="563"/>

  <g class="tag-set tag-set--on-red">
    <use href="#tagFront" filter="url(#tagShadow)"/>
    <text class="side-label" x="720" y="409" font-size="28">BACK:</text>
    <use href="#tagBack" filter="url(#tagShadow)"/>
  </g>

  <g class="tag-set tag-set--on-black">
    <use href="#tagFront" transform="translate(159.5 794.2) scale(0.716)"/>
    <text class="side-label" x="693" y="1101" font-size="22">BACK:</text>
    <use href="#tagBack" transform="translate(175.7 807.9) scale(0.718)"/>
  </g>
</svg>
</body>
</html>
```